Minimalist, Flat(Matte) design for a Beef Jerky packaging company. No bullshit company looking for a

Need a packaging design for a new Beef Jerky product(in English). The name of the company is 'Vellorn' and thus the packaging should reflect the bullish, tough, and simple nature of the beef jerky product. The finished product should communicate simplicity, minimalism, yet toughness and strength.

The logo should be simple, with a minimal number of colors , and should be either all white/cream, or have some red as well. Main colors should be white, cream, tinted red, and matte black. I think 4 colors max would be best. The closest example to an existing package style would be Kessip Noir clove cigarettes( image attached).

It will be on a matte black standing pouch package. See image for package type. Package dimensions:

Dimension: Width x Gusset x Height
INCH : 5.125" (W) x 3.125" (G) x 8.125" (H)
MILLIMETER : 130mm (W) x 80mm (G) x 205mm (H)

I don't have anything totally specific so artistic liberty is encouraged, provided the colors are kept to a minimum and looks consistent with the simple nature of the brand and the matte black packaging.

Also attached an existing beef jerky package with a similar style to what we're looking for.

Industry/Entity Type

It Company

Colors
f59195
ffffff

Requirements
Must have
• Low contrast, flat and minimalist design.
Should not have
• A complicated design with many colors. Gawdy/flashy design. Bright colors. High contrast.

```html
<!DOCTYPE html>
<html lang="en">
<head>
<meta charset="utf-8">
<title>Vellorn Beef Jerky – Pouch Front Colourways</title>
<link rel="stylesheet" href="https://fonts.googleapis.com/css2?family=Archivo:wght@600;800&display=swap">
<style>
  :root {
    --stage: #ffffff;
    --pouch-black: #141011;
    --tint-red: #f59195;
    --white: #ffffff;
  }
  html, body {
    margin: 0;
    padding: 0;
    width: 1200px;
    height: 640px;
    overflow: hidden;
    background: var(--stage);
  }
  .stage {
    position: relative;
    width: 1200px;
    height: 640px;
  }
  .pouch-front {
    position: absolute;
    top: 70px;
    width: 291px;
    height: 460px;
    background: var(--pouch-black);
    font-family: "Archivo", "Helvetica Neue", Arial, sans-serif;
  }
  .pouch-front--one { left: 65px; }
  .pouch-front--two { left: 454px; }
  .pouch-front--three { left: 844px; }

  .brand-mark {
    position: absolute;
    left: 0;
    top: 92px;
    width: 100%;
    text-align: center;
  }
  .brand-name {
    display: block;
    font-weight: 800;
    font-size: 42px;
    line-height: 1;
    letter-spacing: 1px;
    text-transform: uppercase;
  }
  .brand-dot {
    display: block;
    width: 84px;
    height: 84px;
    margin: 18px auto 0;
    border-radius: 50%;
  }

  .product-name {
    position: absolute;
    left: 0;
    top: 0;
    width: 100%;
    height: 100%;
    margin: 0;
    font-weight: 600;
    line-height: 1;
  }
  .product-name__beef {
    position: absolute;
    left: 62px;
    top: 258px;
    font-size: 82px;
    letter-spacing: -3px;
  }
  .product-name__jerky {
    position: absolute;
    left: 43px;
    top: 322px;
    font-size: 59px;
    letter-spacing: -1.5px;
  }

  .pouch-blurb {
    position: absolute;
    left: 0;
    top: 396px;
    width: 100%;
    margin: 0;
    text-align: center;
    font-family: Arial, "Helvetica Neue", sans-serif;
    font-size: 7.4px;
    line-height: 10px;
    color: var(--tint-red);
  }

  /* colourways */
  .is-red { color: var(--tint-red); }
  .is-white { color: var(--white); }
  .dot-red { background: var(--tint-red); }
  .dot-white { background: var(--white); }
</style>
</head>
<body>
<main class="stage">

  <section class="pouch-front pouch-front--one" aria-label="Vellorn beef jerky, red and white colourway">
    <div class="brand-mark">
      <span class="brand-name is-red">Vellorn</span>
      <span class="brand-dot dot-white"></span>
    </div>
    <h1 class="product-name is-red">
      <span class="product-name__beef">BEEF</span>
      <span class="product-name__jerky">JERKY</span>
    </h1>
    <p class="pouch-blurb">Lorem ipsum dolor sit amet, consectetur adipiscing elit, sed do<br>eiusmod tempor incididunt ut labore et dolore magna aliqua</p>
  </section>

  <section class="pouch-front pouch-front--two" aria-label="Vellorn beef jerky, white and red colourway">
    <div class="brand-mark">
      <span class="brand-name is-white">Vellorn</span>
      <span class="brand-dot dot-red"></span>
    </div>
    <h1 class="product-name is-white">
      <span class="product-name__beef">BEEF</span>
      <span class="product-name__jerky">JERKY</span>
    </h1>
    <p class="pouch-blurb">Lorem ipsum dolor sit amet, consectetur adipiscing elit, sed do<br>eiusmod tempor incididunt ut labore et dolore magna aliqua</p>
  </section>

  <section class="pouch-front pouch-front--three" aria-label="Vellorn beef jerky, red mark colourway">
    <div class="brand-mark">
      <span class="brand-name is-red">Vellorn</span>
      <span class="brand-dot dot-red"></span>
    </div>
    <h1 class="product-name is-white">
      <span class="product-name__beef">BEEF</span>
      <span class="product-name__jerky">JERKY</span>
    </h1>
    <p class="pouch-blurb">Lorem ipsum dolor sit amet, consectetur adipiscing elit, sed do<br>eiusmod tempor incididunt ut labore et dolore magna aliqua</p>
  </section>

</main>
</body>
</html>
```